Single-sided business card for restaurant bellwether with new logo made on this site

Business card options with new logo including restaurant name, address, phone number and website. This business card is single-sided only and will be presented at the hostess desk for clients to take. I would like to see options based on a cream card background, a white card background, a yellow card background and a burgundy colored background. It needs to be elegant and traditional.

Target Market(s)

local and international crowd

Industry/Entity Type

restaurant

Contact Information for Business Card

address, website and phone number

Font styles to use
Serif

Colors
EE7325
F08F49
F5BC92
FAE3D3
FDF4ED

Requirements
Must have
• new logo, address, phone number, website
Should not have
• more than three colors

```html
<!DOCTYPE html>
<html lang="es">
<head>
<meta charset="utf-8">
<title>Bellwether – Tarjeta de presentación</title>
<link rel="stylesheet" href="https://fonts.googleapis.com/css2?family=Cinzel:wght@500;600&family=Cormorant+Garamond:wght@600&family=Arimo&display=swap">
<style>
  :root {
    --backdrop: #b4b4b4;
    --card: #ffffff;
    --ink: #3b1c1a;
    --sun: #f5b12d;
    --rule: #5a3a36;
  }
  * { margin: 0; padding: 0; box-sizing: border-box; }
  html, body {
    width: 1200px; height: 1200px; overflow: hidden;
    background: var(--backdrop);
  }
  .business-card {
    position: absolute;
    left: 379px; top: 238px;
    width: 442px; height: 723px;
    background: var(--card);
    border: 1px solid var(--ink);
    color: var(--ink);
    text-align: center;
  }
  .brand-mark {
    position: absolute;
    left: 151px; top: 113px;
    width: 140px; height: 140px;
    background: var(--sun);
  }
  .brand-name {
    position: absolute;
    left: 0; right: 0; top: 262px;
    font-family: "Cinzel", serif;
    font-weight: 500;
    font-size: 40px;
    line-height: 46px;
    letter-spacing: 0.2em;
    padding-left: 0.2em;
    color: var(--ink);
  }
  .reservations {
    position: absolute;
    left: 0; right: 0; top: 666px;
  }
  .reservations-label {
    position: absolute;
    left: 0; right: 0; top: 428px;
    font-family: "Cinzel", serif;
    font-weight: 600;
    font-size: 24px;
    letter-spacing: 0.02em;
  }
  .reservations-phone {
    position: absolute;
    left: 0; right: 0; top: 454px;
    font-family: "Cormorant Garamond", serif;
    font-weight: 600;
    font-size: 40px;
    letter-spacing: 0.02em;
  }
  .divider {
    position: absolute;
    left: 119px; width: 203px; height: 2px;
    background: linear-gradient(90deg, rgba(90,58,54,0.2), var(--rule) 40%, var(--rule) 60%, rgba(90,58,54,0.2));
  }
  .divider--top { top: 511px; }
  .divider--bottom { top: 650px; }
  .address {
    position: absolute;
    left: 0; right: 0; top: 524px;
    font-family: "Arimo", sans-serif;
    font-style: normal;
    font-size: 20px;
    line-height: 27px;
  }
  .website {
    position: absolute;
    left: 0; right: 0; top: 665px;
    font-family: "Arimo", sans-serif;
    font-size: 19px;
    letter-spacing: 0.01em;
  }
</style>
</head>
<body>
  <main class="business-card">
    <div class="brand-mark"></div>
    <h1 class="brand-name">BELL<br>WETHER</h1>

    <p class="reservations-label">RESERVACIONES</p>
    <p class="reservations-phone">555-014-2271</p>

    <div class="divider divider--top"></div>
    <address class="address">
      Restaurant Bellwether<br>
      Jacaranda 415<br>
      Bahía Serena<br>
      Costa Linda CP 10420
    </address>
    <div class="divider divider--bottom"></div>

    <p class="website">www.bellwether.com.mx</p>
  </main>
</body>
</html>
```